TAILWIND FIELDS Pet Resorts Outdoor Signage

4 x 8 outdoor signage design for our two locations

Target Market(s)

Existing and New Customers

Industry/Entity Type

Pet Care

Font styles to use
Sans Serif

Colors

Designer to choose colors to be used in the design.

```html
<!DOCTYPE html>
<html lang="en">
<head>
<meta charset="utf-8">
<title>TAILWIND FIELDS Pet Resorts – Outdoor Sign</title>
<link rel="stylesheet" href="https://fonts.googleapis.com/css2?family=Montserrat:wght@400;700;800&display=swap">
<style>
  :root {
    --navy: #18113f;
    --orange: #f9ad3e;
    --ink: #111111;
    --white: #ffffff;
    --backdrop: #e7e7e9;
  }
  * { margin: 0; padding: 0; box-sizing: border-box; }
  html, body {
    width: 849px;
    height: 1200px;
    overflow: hidden;
    background: var(--backdrop);
    font-family: "Montserrat", Arial, sans-serif;
  }
  .sign {
    position: absolute;
    left: 149px;
    top: 50px;
    width: 551px;
    height: 1100px;
    background: var(--navy);
  }
  .brand {
    position: absolute;
    left: 50px;
    top: 72px;
    display: flex;
    align-items: center;
    gap: 14px;
  }
  .brand-dot {
    width: 26px;
    height: 26px;
    border-radius: 50%;
    background: var(--orange);
    flex: none;
  }
  .brand-name {
    color: var(--orange);
    font-weight: 800;
    font-size: 58px;
    line-height: 1.02;
    letter-spacing: 0.01em;
  }
  .tagline-box {
    position: absolute;
    left: 46px;
    top: 312px;
    width: 459px;
    height: 120px;
    background: var(--orange);
    color: var(--ink);
    padding: 20px 0 0 27px;
    font-weight: 400;
    font-size: 30px;
    line-height: 44px;
    letter-spacing: 0.04em;
  }
  .services {
    position: absolute;
    left: 44px;
    top: 506px;
    list-style: none;
  }
  .service {
    display: flex;
    align-items: center;
    height: 58px;
    margin-bottom: 27px;
    color: var(--orange);
    font-weight: 800;
    font-size: 46px;
    letter-spacing: 0.03em;
  }
  .service svg { width: 58px; height: 58px; margin-right: 30px; flex: none; }
  .extras {
    position: absolute;
    left: 50px;
    top: 800px;
    color: var(--orange);
    font-weight: 400;
    font-size: 34px;
    line-height: 47px;
    letter-spacing: 0.04em;
  }
  .contact-title {
    position: absolute;
    left: 45px;
    top: 925px;
    color: var(--orange);
    font-weight: 800;
    font-size: 36px;
    letter-spacing: 0.03em;
  }
  .contact-line {
    position: absolute;
    left: 50px;
    display: flex;
    align-items: center;
    color: var(--white);
    font-weight: 700;
    font-size: 26px;
    letter-spacing: 0.02em;
  }
  .contact-line svg { width: 33px; height: 33px; margin-right: 16px; flex: none; }
  .contact-phone { top: 979px; }
  .contact-web { top: 1027px; }
</style>
</head>
<body>
  <main class="sign">
    <div class="brand">
      <span class="brand-dot"></span>
      <div class="brand-name">TAILWIND<br>FIELDS</div>
    </div>

    <div class="tagline-box">
      PET RESORT<br>ALL BREED FRIENDLY
    </div>

    <ul class="services">
      <li class="service">
        <svg viewBox="0 0 60 60" aria-hidden="true"><path d="M55.1 23.3 A26 26 0 1 1 25.5 4.4" fill="none" stroke="#f9ad3e" stroke-width="5" stroke-linecap="round"/><path d="M17 30 L27 40 L50 13" fill="none" stroke="#f9ad3e" stroke-width="5" stroke-linecap="round" stroke-linejoin="round"/></svg>
        BOARDING
      </li>
      <li class="service">
        <svg viewBox="0 0 60 60" aria-hidden="true"><path d="M55.1 23.3 A26 26 0 1 1 25.5 4.4" fill="none" stroke="#f9ad3e" stroke-width="5" stroke-linecap="round"/><path d="M17 30 L27 40 L50 13" fill="none" stroke="#f9ad3e" stroke-width="5" stroke-linecap="round" stroke-linejoin="round"/></svg>
        DAYCARE
      </li>
      <li class="service">
        <svg viewBox="0 0 60 60" aria-hidden="true"><path d="M55.1 23.3 A26 26 0 1 1 25.5 4.4" fill="none" stroke="#f9ad3e" stroke-width="5" stroke-linecap="round"/><path d="M17 30 L27 40 L50 13" fill="none" stroke="#f9ad3e" stroke-width="5" stroke-linecap="round" stroke-linejoin="round"/></svg>
        TRAINING
      </li>
    </ul>

    <p class="extras">FULL-SERVICE SALON<br>PET TAXI &amp; MORE</p>

    <h2 class="contact-title">CONTACT US:</h2>

    <div class="contact-line contact-phone">
      <svg viewBox="0 0 32 32" aria-hidden="true">
        <path d="M7 4 L11.5 4 L13 10 L10.5 12.5 C12 16 15.5 19.5 19.5 21.5 L22 19 L28 20.5 L28 25 C28 27 26.5 28 25 28 C14 27.5 4.5 18 4 7 C4 5.5 5 4 7 4 Z" fill="none" stroke="#ffffff" stroke-width="2.4" stroke-linejoin="round"/>
        <path d="M18 3.5 A11 11 0 0 1 28.5 14" fill="none" stroke="#ffffff" stroke-width="1.8" stroke-linecap="round"/>
        <path d="M18 8 A6.5 6.5 0 0 1 24 14" fill="none" stroke="#ffffff" stroke-width="1.8" stroke-linecap="round"/>
      </svg>
      905-555-0142
    </div>

    <div class="contact-line contact-web">
      <svg viewBox="0 0 32 32" aria-hidden="true" fill="none" stroke="#ffffff" stroke-width="2">
        <circle cx="16" cy="16" r="13.5"/>
        <ellipse cx="16" cy="16" rx="6" ry="13.5"/>
        <line x1="16" y1="2.5" x2="16" y2="29.5"/>
        <line x1="2.5" y1="16" x2="29.5" y2="16"/>
        <line x1="4.5" y1="9" x2="27.5" y2="9"/>
        <line x1="4.5" y1="23" x2="27.5" y2="23"/>
      </svg>
      www.tailwindfields.ca
    </div>
  </main>
</body>
</html>
```